HARD MONEY ORIGINATOR RECRUITMENT.
Looking for individuals to help us originate loans for real estate investor financing primarily used to fix up properties and resell.
HARD MONEY ORIGINATORS WANTED
No Licensing Required
Work As Independent Contractor
1% Flat Finders Fee on Each Loan
Referral Compensation for Recruiting New Originators
Immediate Payouts
Programs Offered Nationwide
Marketing Assistance and Support Available
Email mpelton@brightquaylending.com for more information or call (800) 641-2950 Ext. 24 Brightquay Lending Services, Inc. www.brightquaylending.com NMLS #318760
Industry/Entity Type
Real Estate
Look and feel
Each slider illustrates characteristics of the customer's brand and the style your logo design should communicate.

```html
<!DOCTYPE html>
<html lang="en">
<head>
<meta charset="utf-8">
<title>Hard Money Originator Recruitment</title>
<link href="https://fonts.googleapis.com/css2?family=Arvo:wght@700&family=Lato:wght@400;700;900&display=swap" rel="stylesheet">
<style>
  :root {
    --bg: #e9e6e1;
    --paper: #ffffff;
    --crimson: #d8254f;
    --panel: #ededee;
    --stripe: #d9d9db;
    --ink: #2b2b2b;
    --frame: #0d0d0d;
    --brand: #2f62c8;
  }
  * { margin: 0; padding: 0; box-sizing: border-box; }
  html, body { width: 1200px; height: 1200px; overflow: hidden; background: var(--bg); }
  .flyer {
    position: absolute; left: 180px; top: 50px; width: 840px; height: 1100px;
    background: var(--paper); overflow: hidden;
    box-shadow: 0 6px 24px rgba(0,0,0,.18);
    font-family: "Lato", sans-serif; color: var(--ink);
  }
  .hero-photo {
    position: absolute; left: 0; top: 0; width: 840px; height: 520px;
    background: linear-gradient(180deg, #ecebe8 0%, #e2ddd6 45%, #b08a72 70%, #efeae4 100%);
  }
  .roof { position: absolute; left: 0; top: 380px; width: 840px; height: 200px; }
  .brand {
    position: absolute; left: 0; right: 0; top: 580px;
    display: flex; align-items: center; justify-content: center; gap: 14px;
  }
  .brand-dot { width: 34px; height: 34px; border-radius: 50%; background: var(--brand); }
  .brand-name { font-weight: 900; font-size: 30px; color: var(--brand); letter-spacing: .5px; }
  .title-band {
    position: absolute; left: 0; top: 700px; width: 840px; height: 128px;
    background: var(--crimson);
  }
  .title {
    position: absolute; left: 110px; top: 18px; color: #fff;
    font-family: "Arvo", serif; font-weight: 700; font-size: 42px; line-height: 48px; letter-spacing: 1px;
  }
  .lower {
    position: absolute; left: 0; top: 828px; width: 840px; height: 272px; background: var(--panel);
  }
  .photo-block {
    position: absolute; left: 560px; top: 770px; width: 280px; height: 200px;
    background: var(--frame); border-left: 7px solid var(--crimson);
  }
  .worker-photo {
    position: absolute; left: 38px; top: 22px; width: 220px; height: 156px;
    background: linear-gradient(160deg, #b9b6ae 0%, #8b7d6f 45%, #54446a 100%);
  }
  .benefits {
    position: absolute; left: 110px; top: 846px; list-style: none;
    font-size: 17px; line-height: 24px;
  }
  .benefits li::before { content: "\2713"; margin-right: 10px; }
  .footer {
    position: absolute; left: 100px; right: 30px; top: 1026px;
    display: flex; align-items: center; justify-content: space-between;
  }
  .divider { width: 4px; height: 52px; background: var(--ink); flex: none; }
  .company { font-size: 17px; line-height: 22px; width: 170px; }
  .contact h3 { font-weight: 900; font-size: 16px; line-height: 20px; }
  .contact p { font-size: 14px; line-height: 19px; display: flex; align-items: center; gap: 7px; white-space: nowrap; }
  .contact .phone { color: var(--crimson); }
  .web { font-size: 15px; line-height: 19px; text-align: center; white-space: nowrap; }
  .web svg { display: block; margin: 0 auto 2px; }
</style>
</head>
<body>
<main class="flyer">
  <div class="hero-photo" role="img" aria-label="Photo of a smiling family of four in white clothing on a tufted white headboard bed"></div>
  <svg class="roof" viewBox="0 0 840 200" aria-hidden="true">
    <polygon points="0,145 430,20 840,90 840,200 0,200" fill="var(--paper)"/>
    <polygon points="0,160 430,38 840,108 840,130 430,60 0,182" fill="var(--stripe)"/>
  </svg>
  <div class="brand">
    <span class="brand-dot"></span>
    <span class="brand-name">Brightquay Lending Services, Inc.</span>
  </div>
  <section class="title-band">
    <h1 class="title">HARD MONEY ORIGINATOR<br>RECRUITMENT.</h1>
  </section>
  <div class="lower"></div>
  <div class="photo-block">
    <div class="worker-photo" role="img" aria-label="Photo of a construction worker in a yellow hard hat carrying lumber"></div>
  </div>
  <ul class="benefits">
    <li>No Licensing Required</li>
    <li>Work As Independent Contractor</li>
    <li>1% Flat Finders Fee on Each Loan</li>
    <li>Referral Compensation for Recruiting New Originators</li>
    <li>Immediate Payouts</li>
    <li>Programs Offered Nationwide</li>
    <li>Marketing Assistance and Support Available</li>
  </ul>
  <footer class="footer">
    <div class="company">Brightquay Lending Services, Inc.</div>
    <div class="divider"></div>
    <div class="contact">
      <h3>CONTACT US</h3>
      <p><svg width="13" height="10" viewBox="0 0 13 10"><rect x=".75" y=".75" width="11.5" height="8.5" fill="none" stroke="currentColor" stroke-width="1.5"/><path d="M1 1l5.5 4.5L12 1" fill="none" stroke="currentColor" stroke-width="1.5"/></svg>mpelton@brightquaylending.com</p>
      <p class="phone"><svg width="12" height="12" viewBox="0 0 12 12"><path d="M2 1l2.5 0 1 3-1.5 1a7 7 0 0 0 3 3l1-1.5 3 1V10a1 1 0 0 1-1 1A10 10 0 0 1 1 2a1 1 0 0 1 1-1z" fill="#2b2b2b"/></svg>(800) 641-2950 Ext. 24</p>
    </div>
    <div class="divider"></div>
    <div class="web">
      <svg width="32" height="21" viewBox="0 0 36 24"><rect x="6" y="2" width="24" height="16" rx="1.5" fill="none" stroke="currentColor" stroke-width="2.5"/><rect x="1" y="19" width="34" height="3" rx="1" fill="currentColor"/></svg>
      www.brightquaylending.com<br>NMLS #318760
    </div>
  </footer>
</main>
</body>
</html>
```